Lumo Brisa - Letter Head

My company is a residential and commercial cleaning company , which is located in Abu Dhabi, UAE.
I am looking for a creative letterhead reflects the professional and reflects professionalism and send the feeling of relax and comfort.
The color which will be used it has to be selected carefully in prospective of colors psychological effects, so every color to be used should be for a reason.
Also, reflecting my company colors in an attractive way.
Regarding the information which it should contains, it has to show the address, contacts , telephones an, email address and website.
Also, my company logo is attached

```html
<!DOCTYPE html>
<html lang="en">
<head>
<meta charset="utf-8">
<title>Lumo Brisa – Letterhead</title>
<link href="https://fonts.googleapis.com/css2?family=Arimo:wght@400;700&display=swap" rel="stylesheet">
<style>
  :root {
    --backdrop: #e9eaec;
    --paper: #ffffff;
    --brand-blue: #1565ad;
    --brand-green: #8cc63f;
    --green-light: #c5e17a;
    --ink: #3a3a3a;
    --ink-soft: #6b6b6b;
    --rule: #1565ad;
  }
  html, body {
    margin: 0;
    width: 1200px;
    height: 795px;
    overflow: hidden;
    background: var(--backdrop);
    font-family: "Arimo", Arial, sans-serif;
  }
  .letterhead {
    position: absolute;
    left: 319px;
    top: 0;
    width: 562px;
    height: 795px;
    background: var(--paper);
    box-shadow: 0 2px 14px rgba(0,0,0,0.12);
    overflow: hidden;
    color: var(--ink);
  }
  .brand {
    position: absolute;
    left: 46px;
    top: 62px;
    display: flex;
    align-items: center;
    gap: 8px;
    font-weight: 700;
    font-size: 24px;
    color: var(--brand-blue);
    letter-spacing: -0.3px;
  }
  .brand-dot {
    width: 14px;
    height: 14px;
    border-radius: 50%;
    background: var(--brand-green);
  }
  .contacts {
    position: absolute;
    right: 46px;
    top: 56px;
    border-left: 1px solid var(--rule);
    padding-left: 10px;
    font-size: 7.5px;
    line-height: 12px;
    color: var(--ink-soft);
    list-style: none;
    margin: 0;
  }
  .contacts li { display: flex; align-items: center; gap: 6px; }
  .contacts svg { width: 8px; height: 8px; flex: none; }
  .letter {
    position: absolute;
    left: 70px;
    top: 170px;
    width: 410px;
    font-size: 7.6px;
    line-height: 11px;
  }
  .salutation { font-weight: 700; margin: 0 0 10px; }
  .letter p { margin: 0 0 11px; }
  .sign-off { margin-top: 18px; }
  .signature {
    display: block;
    width: 110px;
    height: 34px;
    margin: 6px 0 0 50px;
    background: linear-gradient(90deg, #f1f1f1, #e4e4e4);
    border-radius: 3px;
  }
  .footer-wave {
    position: absolute;
    left: 0;
    bottom: 0;
    width: 562px;
    height: 230px;
  }
  .address {
    position: absolute;
    right: 30px;
    bottom: 22px;
    color: #ffffff;
    font-size: 10px;
    letter-spacing: 0.2px;
  }
</style>
</head>
<body>
<main class="letterhead">
  <div class="brand"><span class="brand-dot"></span>Lumo Brisa</div>

  <ul class="contacts">
    <li><svg viewBox="0 0 8 8"><path d="M2 0.5h1.5l0.5 2-1 0.8a4 4 0 0 0 1.7 1.7l0.8-1 2 0.5V6a1.5 1.5 0 0 1-1.5 1.5A6 6 0 0 1 0.5 2 1.5 1.5 0 0 1 2 0.5z" fill="var(--brand-green)"/></svg>(+971) 2 555 0148</li>
    <li><svg viewBox="0 0 8 8"><rect x="1" y="2.5" width="6" height="4" rx="0.6" fill="none" stroke="var(--brand-green)"/><rect x="2.3" y="0.8" width="3.4" height="2" fill="var(--brand-green)"/></svg>(+971) 2 555 0149</li>
    <li><svg viewBox="0 0 8 8"><rect x="0.5" y="1.5" width="7" height="5" rx="0.6" fill="var(--brand-green)"/><path d="M0.8 1.9 4 4.4 7.2 1.9" fill="none" stroke="#fff" stroke-width="0.7"/></svg>info@lumobrisa.com</li>
    <li><svg viewBox="0 0 8 8"><circle cx="4" cy="4" r="3.4" fill="none" stroke="var(--brand-green)"/><path d="M0.6 4h6.8M4 0.6c-2 2-2 4.8 0 6.8M4 0.6c2 2 2 4.8 0 6.8" fill="none" stroke="var(--brand-green)" stroke-width="0.6"/></svg>www.lumobrisa.com</li>
  </ul>

  <article class="letter">
    <p class="salutation">Dear Mr. Haddad,</p>
    <p>Lorem ipsum dolor sit amet, consectetuer adipiscing elit, sed diam nonummy nibh euismod tincidunt ut laoreet dolore magna aliquam erat volutpat. Ut wisi enim ad minim veniam, quis nostrud exerci tation ullamcorper suscipit lobortis nisl ut aliquip ex ea commodo consequat. Nam liber tempor cum soluta nobis eleifend option congue nihil imperdiet doming id quod mazim placerat facer possim assum.</p>
    <p>Duis autem vel eum iriure dolor in hendrerit in vulputate velit esse molestie consequat, vel illum dolore eu feugiat nulla facilisis at vero eros et accumsan et iusto odio dignissim qui blandit praesent luptatum zzril delenit augue duis dolore te feugait nulla facilisi. Ut wisi enim ad minim veniam, quis nostrud exerci tation ullamcorper suscipit lobortis nisl ut aliquip ex ea commodo consequat.</p>
    <p>Consectetuer adipiscing elit, sed diam nonummy nibh euismod tincidunt ut laoreet dolore magna aliquam erat volutpat. Ut wisi enim ad minim veniam, quis nostrud exerci tation ullamcorper suscipit lobortis nisl ut aliquip ex ea commodo consequat.</p>
    <p>Dolor sit amet, consectetuer adipiscing elit, sed diam nonummy nibh euismod tincidunt ut laoreet dolore magna aliquam erat volutpat. Nam liber tempor cum soluta nobis eleifend option congue nihil imperdiet doming id quod mazim placerat facer possim assum.</p>
    <p class="sign-off">Sincerely,</p>
    <span class="signature" role="img" aria-label="Handwritten signature of the sender"></span>
  </article>

  <svg class="footer-wave" viewBox="0 0 562 230" preserveAspectRatio="none" aria-hidden="true">
    <path d="M0 196 C160 210 250 170 320 110 C390 50 470 22 562 14 L562 26 C470 34 395 62 328 120 C258 182 165 222 0 212 Z" fill="var(--green-light)"/>
    <path d="M0 202 C160 216 255 176 324 116 C394 56 472 28 562 20 L562 30 C472 38 398 68 332 126 C262 188 168 228 0 216 Z" fill="var(--brand-green)"/>
    <path d="M0 214 C168 226 262 190 332 130 C398 72 474 42 562 34 L562 230 L0 230 Z" fill="var(--brand-blue)"/>
  </svg>
  <p class="address">48 Corniche Road, Suite 210, Abu Dhabi, UAE</p>
</main>
</body>
</html>
```